Cedar Row Maintenance and Concierge Flyer

We need a flyer for cedar row maintenance and concierge service. We specialize in and provide residential maintenance and errand services to retired and semi retired persons living in the Lake Norman area. The services we include:
Lighting and plumbing repairs
Ceiling fan installation
Handicap accessories
Locks and security
Picture hanging
Hang blinds
Furniture arrangement / assembly
Pressure washing
Battery Jump start
and more...

Our Concierge services include:
Errand running
Grocery shopping
Wellness Checks
Dog Walk
Garbage Collection
and more...

We offer monthly service agreements and 24/7 access
Call text or e-mail for more information
704.555.0187
1cedarrowmaint@quillpostmail.com

The design should invoke a sense of trust and a customer service driven mission

Target Market(s)

Residential maintenance

Industry/Entity Type

Property Maintenance

Contact Information for Business Card

Derek Halvorsen
48176 Quimby Ferrel Rd.
Cornelius NC 28031
704.555.0187
with uploaded logo

Requirements
Nice to have
• Would like a postcard size flyer. Front and back
Should not have
• No pics of of people wearing hard hats or pics of blueprints. No pics of commercial or industrial maintenance.

```html
<!DOCTYPE html>
<html lang="en">
<head>
<meta charset="utf-8">
<title>Cedar Row Maintenance and Concierge — Postcard Flyer</title>
<link rel="stylesheet" href="https://fonts.googleapis.com/css2?family=Source+Sans+3:wght@400;600;700&display=swap">
<style>
  :root {
    --backdrop: #e8e2d8;
    --card-white: #ffffff;
    --card-grey: #8a8b8e;
    --band-grey: #8d8e91;
    --brand-red: #d21f26;
    --ink-dark: #3b3b3d;
    --ink-mid: #6d6e71;
    --ink-light: #ffffff;
    --rule: #b9babc;
    --rule-light: #b4b5b7;
  }
  * { box-sizing: border-box; margin: 0; padding: 0; }
  html, body { width: 1200px; height: 1147px; overflow: hidden; }
  body {
    background: var(--backdrop);
    font-family: "Source Sans 3", "Myriad Pro", Arial, sans-serif;
    position: relative;
  }
  .card { position: absolute; overflow: hidden; }

  /* Front */
  .card--front {
    left: 268px; top: 52px; width: 884px; height: 504px;
    background: var(--card-white);
    border-radius: 27px;
    border: 1px solid #9c9c9c;
  }
  .brand {
    position: absolute; left: 185px; top: 58px;
    display: flex; align-items: center; gap: 22px;
  }
  .brand__dot {
    width: 88px; height: 88px; border-radius: 50%;
    border: 9px solid var(--brand-red);
  }
  .brand__name {
    font-size: 34px; font-weight: 400; color: var(--ink-mid);
    line-height: 1.15; letter-spacing: 0.5px;
  }
  .person {
    position: absolute; right: calc(884px - 349px); top: 268px;
    text-align: right; white-space: nowrap;
  }
  .person__name { font-size: 32px; font-weight: 700; color: var(--ink-dark); line-height: 1; }
  .person__title { font-size: 23px; color: var(--ink-mid); margin-top: 8px; line-height: 1; }
  .front-divider {
    position: absolute; left: 371px; top: 244px; width: 1px; height: 129px;
    background: var(--rule);
  }
  .contact-list {
    position: absolute; left: 400px; top: 254px; list-style: none;
  }
  .contact-list li {
    display: flex; align-items: center; gap: 8px;
    height: 40px; font-size: 22px; color: var(--ink-dark);
  }
  .contact-list svg { width: 18px; height: 18px; flex: none; }
  .address-band {
    position: absolute; left: 0; right: 0; top: 403px; height: 59px;
    border-top: 2px solid var(--brand-red);
    border-bottom: 2px solid var(--brand-red);
    background: linear-gradient(var(--card-white) 0 5px, var(--band-grey) 5px calc(100% - 5px), var(--card-white) calc(100% - 5px));
    display: flex; align-items: center; justify-content: center;
    color: var(--ink-light); font-size: 21px;
  }

  /* Back */
  .card--back {
    left: 53px; top: 619px; width: 882px; height: 503px;
    background: var(--card-grey);
    border-radius: 48px;
  }
  .back-mark {
    position: absolute; left: 36px; top: 96px; width: 238px; height: 238px;
    border-radius: 50%; border: 12px solid var(--brand-red);
    display: flex; align-items: center; justify-content: center; text-align: center;
  }
  .back-mark__name {
    font-size: 23px; font-weight: 400; color: var(--ink-light); line-height: 1.2;
  }
  .back-divider {
    position: absolute; top: 62px; width: 1px; height: 330px;
    background: var(--rule-light);
  }
  .back-divider--first { left: 296px; }
  .back-divider--second { left: 642px; }
  .service-group { position: absolute; top: 58px; }
  .service-group--maintenance { left: 316px; }
  .service-group--concierge { left: 660px; }
  .service-group__heading {
    font-size: 19px; font-weight: 700; color: var(--ink-light);
    letter-spacing: 1.5px; text-transform: uppercase;
    height: 32px; line-height: 24px;
    border-bottom: 2px solid var(--brand-red);
    display: inline-block; margin-bottom: 6px;
  }
  .service-list { list-style: none; }
  .service-list li {
    display: flex; align-items: center; gap: 10px;
    height: 30px; font-size: 19px; color: var(--ink-light); white-space: nowrap;
  }
  .service-list svg { width: 18px; height: 13px; flex: none; }
  .back-note {
    position: absolute; left: 0; right: 0; top: 402px; text-align: center;
    font-size: 17px; color: var(--ink-light);
  }
  .back-web {
    position: absolute; left: 0; right: 0; top: 430px; text-align: center;
    font-size: 28px; letter-spacing: 6px; color: var(--ink-light);
  }
</style>
</head>
<body>

<section class="card card--front" aria-label="Flyer front">
  <div class="brand">
    <span class="brand__dot" aria-hidden="true"></span>
    <div class="brand__name">Cedar Row<br>Maintenance &amp; Concierge</div>
  </div>

  <div class="person">
    <p class="person__name">Derek Halvorsen</p>
    <p class="person__title">Owner</p>
  </div>

  <div class="front-divider"></div>

  <ul class="contact-list">
    <li>
      <svg viewBox="0 0 24 24" aria-hidden="true"><path fill="#d21f26" d="M6.6 10.8a15 15 0 0 0 6.6 6.6l2.2-2.2c.3-.3.7-.4 1-.2 1.1.4 2.3.6 3.6.6.6 0 1 .4 1 1V20c0 .6-.4 1-1 1A17 17 0 0 1 3 4c0-.6.4-1 1-1h3.5c.6 0 1 .4 1 1 0 1.3.2 2.5.6 3.6.1.3 0 .7-.2 1z"/></svg>
      704.555.0187
    </li>
    <li>
      <svg viewBox="0 0 24 24" aria-hidden="true"><rect x="2" y="5" width="20" height="14" rx="2" fill="#d21f26"/><path d="M3 6l9 7 9-7" stroke="#fff" stroke-width="2" fill="none"/></svg>
      1cedarrowmaint@quillpostmail.com
    </li>
    <li>
      <svg viewBox="0 0 24 24" aria-hidden="true" fill="none" stroke="#d21f26" stroke-width="2"><circle cx="12" cy="12" r="9.5"/><ellipse cx="12" cy="12" rx="4" ry="9.5"/><path d="M2.5 12h19M4 7h16M4 17h16"/></svg>
      www.1cedarrowmaint.com
    </li>
  </ul>

  <div class="address-band">48176 Quimby Ferrel Rd., Cornelius NC 28031</div>
</section>

<section class="card card--back" aria-label="Flyer back">
  <div class="back-mark">
    <p class="back-mark__name">Cedar Row<br>Maintenance &amp;<br>Concierge</p>
  </div>

  <div class="back-divider back-divider--first"></div>

  <div class="service-group service-group--maintenance">
    <p class="service-group__heading">Maintenance</p>
    <ul class="service-list">
      <li><svg viewBox="0 0 22 16" aria-hidden="true"><path d="M2 8l6 6L20 2" stroke="#fff" stroke-width="3" fill="none"/></svg>Lighting and plumbing repairs</li>
      <li><svg viewBox="0 0 22 16" aria-hidden="true"><path d="M2 8l6 6L20 2" stroke="#fff" stroke-width="3" fill="none"/></svg>Ceiling fan installation</li>
      <li><svg viewBox="0 0 22 16" aria-hidden="true"><path d="M2 8l6 6L20 2" stroke="#fff" stroke-width="3" fill="none"/></svg>Handicap accessories</li>
      <li><svg viewBox="0 0 22 16" aria-hidden="true"><path d="M2 8l6 6L20 2" stroke="#fff" stroke-width="3" fill="none"/></svg>Locks and security</li>
      <li><svg viewBox="0 0 22 16" aria-hidden="true"><path d="M2 8l6 6L20 2" stroke="#fff" stroke-width="3" fill="none"/></svg>Picture hanging</li>
      <li><svg viewBox="0 0 22 16" aria-hidden="true"><path d="M2 8l6 6L20 2" stroke="#fff" stroke-width="3" fill="none"/></svg>Hang blinds</li>
      <li><svg viewBox="0 0 22 16" aria-hidden="true"><path d="M2 8l6 6L20 2" stroke="#fff" stroke-width="3" fill="none"/></svg>Furniture arrangement / assembly</li>
      <li><svg viewBox="0 0 22 16" aria-hidden="true"><path d="M2 8l6 6L20 2" stroke="#fff" stroke-width="3" fill="none"/></svg>Pressure washing</li>
      <li><svg viewBox="0 0 22 16" aria-hidden="true"><path d="M2 8l6 6L20 2" stroke="#fff" stroke-width="3" fill="none"/></svg>Battery Jump start</li>
    </ul>
  </div>

  <div class="back-divider back-divider--second"></div>

  <div class="service-group service-group--concierge">
    <p class="service-group__heading">Concierge</p>
    <ul class="service-list">
      <li><svg viewBox="0 0 22 16" aria-hidden="true"><path d="M2 8l6 6L20 2" stroke="#fff" stroke-width="3" fill="none"/></svg>Errand running</li>
      <li><svg viewBox="0 0 22 16" aria-hidden="true"><path d="M2 8l6 6L20 2" stroke="#fff" stroke-width="3" fill="none"/></svg>Grocery shopping</li>
      <li><svg viewBox="0 0 22 16" aria-hidden="true"><path d="M2 8l6 6L20 2" stroke="#fff" stroke-width="3" fill="none"/></svg>Wellness Checks</li>
      <li><svg viewBox="0 0 22 16" aria-hidden="true"><path d="M2 8l6 6L20 2" stroke="#fff" stroke-width="3" fill="none"/></svg>Dog Walk</li>
      <li><svg viewBox="0 0 22 16" aria-hidden="true"><path d="M2 8l6 6L20 2" stroke="#fff" stroke-width="3" fill="none"/></svg>Garbage Collection</li>
      <li><svg viewBox="0 0 22 16" aria-hidden="true"><path d="M2 8l6 6L20 2" stroke="#fff" stroke-width="3" fill="none"/></svg>and more...</li>
    </ul>
  </div>

  <p class="back-note">Monthly service agreements &amp; 24/7 access · Call, text or e-mail 704.555.0187</p>
  <p class="back-web">www.1cedarrowmaint.com</p>
</section>

</body>
</html>
```